stationary
envelopes, letterhead, biz card
I need single sided standard sized Business Card [3.5" x 2"]
doesnt matter whatever looks good
Professional
Marten Olufsson
President
4218 Wexhollow Ave Ste 202-517
marten@bexlin.com
www.bexlin.com

```html
<!DOCTYPE html>
<html lang="en">
<head>
<meta charset="utf-8">
<title>Bexlin Business Card</title>
<link href="https://fonts.googleapis.com/css2?family=Questrial&display=swap" rel="stylesheet">
<style>
  :root {
    --stage: #d9dadc;
    --card-light: #ffffff;
    --card-shade: #e4e5e7;
    --band-dark: #111214;
    --accent-blue: #1a9fd8;
    --ink: #2a2b2e;
    --ink-soft: #5a5c60;
    --name-white: #ffffff;
    --title-grey: #b8babd;
  }
  * { box-sizing: border-box; margin: 0; padding: 0; }
  html, body {
    width: 1200px; height: 901px; overflow: hidden;
    background: var(--stage);
    font-family: "Questrial", "Century Gothic", sans-serif;
  }
  .canvas { position: relative; width: 1200px; height: 901px; }
  .card {
    position: absolute; left: 285px; width: 630px; height: 360px;
    border-radius: 16px; overflow: hidden;
    background: linear-gradient(160deg, var(--card-light) 40%, var(--card-shade) 100%);
    box-shadow: 0 10px 28px rgba(0,0,0,0.18);
  }
  .card-back { top: 40px; }
  .card-front { top: 470px; }
  .card-art { position: absolute; inset: 0; width: 100%; height: 100%; }

  .brand { position: absolute; display: flex; align-items: center; gap: 14px; }
  .brand-mark { width: 22px; height: 22px; background: var(--accent-blue); }
  .brand-name {
    font-size: 48px; color: var(--ink); letter-spacing: 1px; font-weight: 400;
  }
  .card-back .brand { left: 50%; top: 50%; transform: translate(-50%, -50%); }
  .card-front .brand { left: 40px; top: 205px; }
  .card-front .brand-name { font-size: 42px; }

  .holder { position: absolute; right: 26px; top: 16px; text-align: right; }
  .holder-name { color: var(--name-white); font-size: 17px; }
  .holder-title { color: var(--title-grey); font-size: 12px; margin-top: 3px; }

  .contact {
    position: absolute; left: 300px; top: 220px;
    font-size: 13px; line-height: 19px; color: var(--ink-soft);
  }
  .address {
    position: absolute; left: 460px; top: 220px;
    font-size: 13px; line-height: 19px; color: var(--ink-soft);
  }
  .web {
    position: absolute; left: 300px; top: 300px;
    font-size: 13px; color: var(--ink-soft);
  }
</style>
</head>
<body>
<main class="canvas">
  <section class="card card-back" aria-label="Business card back">
    <div class="brand">
      <span class="brand-mark"></span>
      <span class="brand-name">BEXLIN</span>
    </div>
  </section>

  <section class="card card-front" aria-label="Business card front">
    <svg class="card-art" viewBox="0 0 630 360" preserveAspectRatio="none" aria-hidden="true">
      <path d="M0 0 H630 V62 C460 70 250 88 0 112 Z" fill="var(--band-dark)"/>
      <path d="M0 130 C200 104 420 82 630 76 V86 C420 94 210 118 0 146 Z" fill="var(--accent-blue)"/>
      <path d="M0 156 C210 128 420 104 630 96" fill="none" stroke="var(--accent-blue)" stroke-width="2"/>
    </svg>

    <div class="holder">
      <p class="holder-name">Marten Olufsson</p>
      <p class="holder-title">President</p>
    </div>

    <div class="brand">
      <span class="brand-mark"></span>
      <span class="brand-name">BEXLIN</span>
    </div>

    <div class="contact">
      <p>P: 555.014.2280</p>
      <p>F: 555.017.6341</p>
      <p>E: marten@bexlin.com</p>
    </div>
    <div class="address">
      <p>4218 Wexhollow Ave</p>
      <p>Ste 202-517</p>
    </div>
    <p class="web">www.bexlin.com</p>
  </section>
</main>
</body>
</html>
```